Business card and stationery design

Harbourlight Gatherings Co. is a leading event and conference design and management company.
Please view lumorahostgroup.com.au

The business cards needs to convey:
- professionalism and competency
- exclusivity
- memorable experiences and quality

The business card needs to have the following aspects:
- double sided
- Full colour CMYK
- Printed on either high gloss matt card (designer to recommend)

For the business stationery we require:
- Letterhead with top banner and bottom footer
- A thank you card design
- a with compliments slip design
- a MS powerpoint and MS publisher client presentation slide design which includes cover page and then a standard presentation page
(Note- we do NOT require an envelope design- who sends letters these days!)

The company image is using the key colours of gold, silver and black.
A black background to the business card has been used before and is preferred although we are open to options.

Target Market(s)

High end corporations and businesses that require their events and conferences to be exceptionally well designed and managed

Industry/Entity Type

Business

Contact Information for Business Card

FRONT:

Darian Whitlock
- Event and Conference Specialist

Mobile- +61 (0) 491 238 604
Office- 1300 617 482
dariannw@lumorahostgroup.com.au

Web- lumorahostgroup.com.au

BACK:

- Event and

Font styles to use
Other font styles liked:
• The logo designer used Trajan Pro Bold 3 for the font text in the logo

Requirements
Must have
• Amazing design of the following:
• - business card (double sided)
• - letterhead
• - client thank you card
• - powerpoint and publisher client presentation design files

```html
<!DOCTYPE html>
<html lang="en">
<head>
<meta charset="utf-8">
<title>Harbourlight Gatherings Co. – Business Card</title>
<link rel="stylesheet" href="https://fonts.googleapis.com/css2?family=Cinzel:wght@600;700&family=Open+Sans:wght@400&display=swap">
<style>
  :root {
    --backdrop: #4a4a4a;
    --card-white: #ffffff;
    --card-black: #0b0b0b;
    --gold: #c9a94e;
    --gold-light: #e4d196;
    --silver: #9a9a9a;
    --silver-light: #d8d8d8;
    --text-dark: #222222;
    --text-light: #f2f2f2;
  }
  * { margin: 0; padding: 0; box-sizing: border-box; }
  html, body { width: 1200px; height: 820px; overflow: hidden; }
  body {
    background: var(--backdrop);
    position: relative;
    font-family: "Open Sans", Arial, sans-serif;
  }
  .card {
    position: absolute;
    top: 258px;
    width: 477px;
    height: 272px;
    overflow: hidden;
    box-shadow: 0 4px 10px rgba(0,0,0,0.45);
  }
  .card-front { left: 115px; background: var(--card-white); }
  .card-back { left: 621px; background: var(--card-black); }

  .front-wave { position: absolute; inset: 0; width: 100%; height: 100%; }

  .brand-mark {
    position: absolute;
    border-radius: 50%;
    background: var(--gold);
  }
  .front-mark { left: 80px; top: 28px; width: 70px; height: 70px; }
  .brand-name {
    position: absolute;
    font-family: "Cinzel", "Times New Roman", serif;
    font-weight: 700;
    color: var(--silver);
    white-space: nowrap;
    text-align: center;
  }
  .front-name { left: 20px; width: 190px; top: 136px; font-size: 11.5px; letter-spacing: 0.2px; }

  .person {
    position: absolute;
    right: 40px;
    top: 48px;
    text-align: right;
  }
  .person-name {
    font-family: "Cinzel", "Times New Roman", serif;
    font-weight: 700;
    font-size: 19px;
    color: var(--gold);
    letter-spacing: 0.3px;
    line-height: 1.1;
  }
  .person-role { font-size: 11px; color: var(--text-dark); margin-top: 5px; }

  .contact-list {
    position: absolute;
    right: 34px;
    top: 177px;
    list-style: none;
    text-align: right;
  }
  .contact-item {
    font-size: 11.5px;
    color: var(--text-light);
    height: 18.5px;
    line-height: 18.5px;
    display: flex;
    justify-content: flex-end;
    align-items: center;
    gap: 9px;
  }
  .contact-icon { width: 11px; height: 11px; flex: none; }

  .back-pattern {
    position: absolute;
    inset: 0;
    background: radial-gradient(circle at 50% 42%, #2a2a2a 0%, #161616 45%, #080808 100%);
  }
  .back-mark { left: 188px; top: 56px; width: 100px; height: 100px; }
  .back-name { left: 0; width: 100%; top: 180px; font-size: 19px; color: var(--silver-light); }
</style>
</head>
<body>

  <section class="card card-front" aria-label="Business card front">
    <svg class="front-wave" viewBox="0 0 477 272" preserveAspectRatio="none" aria-hidden="true">
      <defs>
        <linearGradient id="silverBand" x1="0" y1="0" x2="1" y2="0">
          <stop offset="0" stop-color="#cfcfcf"/>
          <stop offset="0.5" stop-color="#8e8e8e"/>
          <stop offset="1" stop-color="#d9d9d9"/>
        </linearGradient>
      </defs>
      <path d="M0,166 C110,205 230,192 320,148 C380,120 430,116 477,118 L477,272 L0,272Z" fill="var(--gold-light)"/>
      <path d="M0,180 C120,218 240,198 330,156 C390,130 435,126 477,131 L477,272 L0,272Z" fill="url(#silverBand)"/>
      <path d="M0,210 C130,226 250,206 340,166 C400,141 440,138 477,141 L477,272 L0,272Z" fill="var(--card-black)"/>
    </svg>

    <div class="brand-mark front-mark" aria-hidden="true"></div>
    <div class="brand-name front-name">Harbourlight Gatherings Co.</div>

    <div class="person">
      <div class="person-name">DARIAN WHITLOCK</div>
      <div class="person-role">Event and Conference Specialist</div>
    </div>

    <ul class="contact-list">
      <li class="contact-item">1300 617 482
        <svg class="contact-icon" viewBox="0 0 12 12" aria-hidden="true"><path d="M2.5 1 L4.5 1 L5.2 3.6 L3.9 4.6 C4.6 6.1 5.9 7.4 7.4 8.1 L8.4 6.8 L11 7.5 L11 9.5 C11 10.4 10.3 11 9.5 11 C5 11 1 7 1 2.5 C1 1.7 1.6 1 2.5 1Z" fill="var(--gold)"/></svg>
      </li>
      <li class="contact-item">+61 (0) 491 238 604
        <svg class="contact-icon" viewBox="0 0 12 12" aria-hidden="true"><rect x="3" y="0.5" width="6" height="11" rx="1" fill="none" stroke="var(--gold)" stroke-width="1.2"/><circle cx="6" cy="9.6" r="0.7" fill="var(--gold)"/></svg>
      </li>
      <li class="contact-item">dariannw@lumorahostgroup.com.au
        <svg class="contact-icon" viewBox="0 0 12 12" aria-hidden="true"><rect x="0.5" y="2.5" width="11" height="7.5" fill="var(--gold)"/><path d="M0.8 2.8 L6 6.8 L11.2 2.8" fill="none" stroke="var(--card-black)" stroke-width="0.9"/></svg>
      </li>
      <li class="contact-item">lumorahostgroup.com.au
        <svg class="contact-icon" viewBox="0 0 12 12" aria-hidden="true"><circle cx="6" cy="6" r="5.3" fill="var(--gold)"/><path d="M1 6 H11 M6 0.8 C3.5 3.5 3.5 8.5 6 11.2 M6 0.8 C8.5 3.5 8.5 8.5 6 11.2" fill="none" stroke="var(--card-black)" stroke-width="0.7"/></svg>
      </li>
    </ul>
  </section>

  <section class="card card-back" aria-label="Business card back">
    <div class="back-pattern" role="img" aria-label="Faint spiral of soft dark circles across the black background"></div>
    <div class="brand-mark back-mark" aria-hidden="true"></div>
    <div class="brand-name back-name">Harbourlight Gatherings Co.</div>
  </section>

</body>
</html>
```